Far-Ridge Brokerage Business Cards

We have had success with our logo design and are looking to have a creative business card made. Logo must be prominent in the business card design. We would like headshots to be on the business card, but do not want the photo to be framed at all. We are looking for designs for two different people, so I will attach headshots

Target Market(s)

Home Buyers. Trying to market to younger/trendy crowd. 25-45 year of age.

Industry/Entity Type

Real Estate

Contact Information for Business Card

New business card design needed. Looking for a vibrant and attractive business card.

Font styles to use
Other font styles liked:
• Match the logo font on the Far-Ridge PDQ Realty logo

Requirements
Must have
• Must have sketch swarm logo incorporated. Fair Dwelling Logo should be very small and should be on the back of the card and is a requirement. Propertist logo should be small and on the back of the card with FD logo.

2 different business cards, must have the following info:
Business card 1:
Gary Pelloway & Marla Ventrisch
(555) 208-4417
Marla@frp.example
Marla.lakeviewdwellingsonmarket.example
7283 W Larchmere St, Brindlefield, WI 53999

Business card 2:
Dominic Varseth
(555) 734-2190
Dom@frp.example
Dominic.lakeviewdwellingsonmarket.example

```html
<!DOCTYPE html>
<html lang="en">
<head>
<meta charset="utf-8">
<title>Far-Ridge PDQ Realty – Business Card</title>
<link rel="stylesheet" href="https://fonts.googleapis.com/css2?family=Montserrat:wght@600;700&family=Arimo:wght@400&display=swap">
<style>
  :root {
    --navy: #06203f;
    --orange: #f8a51c;
    --white: #ffffff;
    --stage: #e9ebee;
    --photo-light: #d9d7d3;
    --photo-dark: #9c9791;
  }
  * { box-sizing: border-box; margin: 0; padding: 0; }
  html, body { width: 1200px; height: 801px; overflow: hidden; }
  body { background: var(--stage); position: relative; font-family: "Arimo", Arial, sans-serif; }

  .card { position: absolute; top: 274px; width: 443px; height: 263px; overflow: hidden; }
  .card-front { left: 153px; background: var(--white); }
  .card-back { left: 625px; background: var(--navy); }

  /* Front */
  .front-lower { position: absolute; left: 0; top: 130px; width: 443px; height: 133px; background: var(--navy); }
  .accent-stripe { position: absolute; left: 0; top: 130px; width: 290px; height: 4px; background: var(--orange); }
  .brand { position: absolute; display: flex; align-items: center; gap: 10px; }
  .front-brand { left: 22px; top: 36px; }
  .brand-dot { width: 50px; height: 50px; border-radius: 50%; background: var(--orange); flex: none; }
  .brand-name { font-family: "Montserrat", sans-serif; font-weight: 700; color: var(--navy); font-size: 22px; line-height: 1.05; letter-spacing: 0.3px; }
  .headshot { position: absolute; left: 236px; top: 14px; width: 207px; height: 249px;
    background: linear-gradient(180deg, var(--photo-light) 0%, var(--photo-dark) 100%);
    border-radius: 90px 90px 0 0; }
  .agent-name { position: absolute; left: 27px; top: 150px; font-family: "Montserrat", sans-serif; font-weight: 700; color: var(--orange); font-size: 15.5px; letter-spacing: 0.2px; }
  .contact { position: absolute; left: 27px; top: 177px; color: var(--white); font-size: 12.5px; line-height: 16px; }
  .contact-row { display: flex; align-items: center; gap: 6px; }
  .contact-row svg { width: 12px; height: 12px; flex: none; }
  .address { margin-top: 9px; }

  /* Back */
  .back-brand { left: 0; top: 40px; width: 443px; flex-direction: column; gap: 10px; }
  .back-brand .brand-dot { width: 62px; height: 62px; }
  .back-brand .brand-name { color: var(--white); font-size: 27px; text-align: center; }
  .web-band { position: absolute; left: 0; top: 169px; width: 443px; height: 21px; background: var(--orange);
    color: var(--white); font-size: 12px; letter-spacing: 1.1px; text-align: center; line-height: 21px; }
  .badge-row { position: absolute; left: 0; top: 203px; width: 443px; display: flex; justify-content: center; align-items: center; gap: 8px; }
  .badge-rule { width: 50px; height: 1px; background: rgba(255,255,255,0.25); }
  .badge { background: var(--white); }
  .badge-fair { width: 44px; height: 40px; clip-path: polygon(50% 0, 100% 40%, 100% 100%, 0 100%, 0 40%); }
  .badge-prop { width: 32px; height: 38px; }
</style>
</head>
<body>
  <section class="card card-front">
    <div class="front-lower"></div>
    <div class="accent-stripe"></div>
    <div class="brand front-brand">
      <span class="brand-dot"></span>
      <span class="brand-name">FAR-RIDGE<br>PDQ REALTY</span>
    </div>
    <div class="headshot" role="img" aria-label="Headshot of agent Dominic Varseth, cut out without a frame"></div>
    <h1 class="agent-name">DOMINIC VARSETH</h1>
    <div class="contact">
      <p class="contact-row">
        <svg viewBox="0 0 24 24" aria-hidden="true"><path fill="#f8a51c" d="M6.6 10.8a15 15 0 0 0 6.6 6.6l2.2-2.2a1 1 0 0 1 1-.25 11.4 11.4 0 0 0 3.6.57 1 1 0 0 1 1 1V20a1 1 0 0 1-1 1A17 17 0 0 1 3 4a1 1 0 0 1 1-1h3.5a1 1 0 0 1 1 1c0 1.25.2 2.45.57 3.57a1 1 0 0 1-.25 1z"/></svg>
        (555) 734-2190
      </p>
      <p class="contact-row">
        <svg viewBox="0 0 24 24" aria-hidden="true"><path fill="#f8a51c" d="M2 5h20v14H2z"/><path fill="none" stroke="#06203f" stroke-width="2" d="M2 5l10 8 10-8"/></svg>
        Dom@frp.example
      </p>
      <p class="address">7283 W Larchmere St<br>Brindlefield, WI 53999</p>
    </div>
  </section>

  <section class="card card-back">
    <div class="brand back-brand">
      <span class="brand-dot"></span>
      <span class="brand-name">FAR-RIDGE PDQ REALTY</span>
    </div>
    <p class="web-band">Dominic.lakeviewdwellingsonmarket.example</p>
    <div class="badge-row">
      <span class="badge-rule"></span>
      <span class="badge badge-fair" role="img" aria-label="Fair Dwelling badge"></span>
      <span class="badge badge-prop" role="img" aria-label="Propertist badge"></span>
      <span class="badge-rule"></span>
    </div>
  </section>
</body>
</html>
```